Natural deodorant label

Natural clean deodorant line. Need modernize label which can be sized for both the regular and travel size deodorants. 2.75 x 3" and 1x2". Important to highlight no baking soda and its natural. Also has no aluminum, preservatives, nor chemicals. Its gender inclusive and safe for all ages. Please see website at www.lorvatique.com. will attach current label. Will need a label that i would be able to update with new scents as they come. Want a clean look.
Updates

Need extra days to review

Target Market(s)

the working mother/wife that lives a clean healthy life and pushes that for her family

Industry/Entity Type

health and beauty/deodorant/natural

Colors

Designer to choose colors to be used in the design.

Requirements
Must have
• No baking soda and gender inclusive on label. Clean look. Very little to no picture art.
Nice to have
• Potentially a different color representing the different scents. A brief description of the deodorant scent underneath the scent name. This can be found under the drop down menu titled valdora deodorant scents on the website www.lorvatique.com. Area on front label for a small barcode.
Should not have
• misspelled words; dark label

```html
<!DOCTYPE html>
<html lang="en">
<head>
<meta charset="UTF-8">
<title>Lorvatique Natural Clean Deodorant – Label</title>
<link href="https://fonts.googleapis.com/css2?family=Jost:ital,wght@0,300;0,400;0,500;1,400&display=swap" rel="stylesheet">
<style>
  :root {
    --plum: #744a7c;
    --ink: #111111;
    --paper: #fbfbfb;
    --night: #050505;
    --stage: #e8e8eb;
    --white: #ffffff;
  }
  * { margin: 0; padding: 0; box-sizing: border-box; }
  html, body {
    width: 1200px; height: 1200px; overflow: hidden;
    background: var(--stage);
    font-family: "Jost", "Futura", sans-serif;
  }
  .canvas {
    width: 1200px; height: 1200px;
    display: flex; align-items: center; justify-content: center; gap: 80px;
  }
  .label-slot { width: 440px; height: 650px; position: relative; }
  .label {
    position: absolute; top: 0; left: 0;
    width: 413px; height: 610px;
    transform: scale(1.0654); transform-origin: top left;
    overflow: hidden;
  }
  .label--light { background: linear-gradient(90deg, #f1f0ef 0%, #f4f3f2 50%, var(--paper) 50%, var(--white) 100%); color: var(--ink); }
  .label--dark { background: var(--night); color: var(--white); border: 1.5px solid var(--plum); }

  .rule { position: absolute; left: 19px; right: 19px; height: 7px; background: var(--plum); }
  .rule--top { top: 39px; }
  .rule--bottom { top: 569px; }

  .brand {
    position: absolute; top: 82px; left: 0; right: 0;
    display: flex; flex-direction: column; align-items: center; gap: 10px;
  }
  .brand__dot { width: 30px; height: 30px; border-radius: 50%; background: currentColor; }
  .brand__name {
    font-size: 17px; font-weight: 500; letter-spacing: 1.5px; text-transform: uppercase;
  }

  .product-line {
    position: absolute; top: 180px; left: 0; right: 0; text-align: center;
    font-size: 31px; font-weight: 300; color: var(--plum); line-height: 1;
  }
  .product-type {
    position: absolute; top: 214px; left: 53px; width: 307px; height: 50px;
    background: var(--plum); color: var(--white);
    font-size: 46px; font-weight: 400; line-height: 50px; text-align: center; letter-spacing: 0.5px;
  }

  .free-from {
    position: absolute; top: 301px; left: 112px; list-style: none;
    font-size: 24px; font-style: italic; color: var(--plum); line-height: 26px;
  }

  .scent {
    position: absolute; top: 438px; left: 0; right: 0; text-align: center;
    font-size: 35px; font-weight: 300; letter-spacing: -0.5px; line-height: 1;
  }

  .badges {
    position: absolute; top: 505px; left: 0; right: 0;
    display: flex; justify-content: center; gap: 7px;
  }
  .badge { width: 54px; height: 54px; border-radius: 50%; }
  .label--light .badge { background: var(--ink); }
  .label--dark .badge { background: var(--plum); }
</style>
</head>
<body>
<main class="canvas">
  <div class="label-slot">
    <section class="label label--light">
      <div class="rule rule--top"></div>
      <div class="brand"><span class="brand__dot"></span><span class="brand__name">Lorvatique</span></div>
      <p class="product-line">Natural Clean</p>
      <h1 class="product-type">DEODORANT</h1>
      <ul class="free-from">
        <li>No aluminum</li>
        <li>No chemicals</li>
        <li>No baking soda</li>
        <li>No preservatives</li>
      </ul>
      <p class="scent">UNSCENTED</p>
      <div class="badges">
        <span class="badge" role="img" aria-label="Vegan badge"></span>
        <span class="badge" role="img" aria-label="Cruelty free badge"></span>
        <span class="badge" role="img" aria-label="Unisex badge"></span>
      </div>
      <div class="rule rule--bottom"></div>
    </section>
  </div>
  <div class="label-slot">
    <section class="label label--dark">
      <div class="rule rule--top"></div>
      <div class="brand"><span class="brand__dot"></span><span class="brand__name">Lorvatique</span></div>
      <p class="product-line">Natural Clean</p>
      <h1 class="product-type">DEODORANT</h1>
      <ul class="free-from">
        <li>No aluminum</li>
        <li>No chemicals</li>
        <li>No baking soda</li>
        <li>No preservatives</li>
      </ul>
      <p class="scent">UNSCENTED</p>
      <div class="badges">
        <span class="badge" role="img" aria-label="Vegan badge"></span>
        <span class="badge" role="img" aria-label="Cruelty free badge"></span>
        <span class="badge" role="img" aria-label="Unisex badge"></span>
      </div>
      <div class="rule rule--bottom"></div>
    </section>
  </div>
</main>
</body>
</html>
```